Website design project for ICT Business - Harbor Link Ko

We need website built for our new startup. The company name is Harbor Link KO. Harbor Link is an Information Communication Technology business that aims to help small to medium businesses unlock the power and benefits of the cloud. We are a sales and support business that consults with our clients to assist them in migrating to the cloud safely and without business interruption.

Coding

Coded - Design and coding required

Number of Pages Required

4 page

```html
<!DOCTYPE html>
<html lang="en">
<head>
<meta charset="utf-8">
<title>Harbor Link KO – Information Communication Technology</title>
<link href="https://fonts.googleapis.com/css2?family=Montserrat:wght@400;500;600;700&family=Open+Sans:wght@400;600;700&display=swap" rel="stylesheet">
<style>
:root{
  --blue:#0b9ee0;
  --navy:#0a5ea8;
  --deep:#083f7a;
  --ink:#222;
  --muted:#555;
  --pale:#e6f4fc;
  --line:#d9d9d9;
  --white:#fff;
}
*{margin:0;padding:0;box-sizing:border-box}
html,body{width:715px;height:1200px;overflow:hidden;background:var(--white)}
body{position:relative;font-family:"Open Sans",sans-serif;color:var(--ink)}
.abs{position:absolute}

.topbar{left:0;top:0;width:715px;height:14px;border-bottom:1px solid #cfe3f2;font-size:6px;color:var(--navy)}
.topbar span{position:absolute;top:3px;display:flex;align-items:center;gap:3px}
.header{left:0;top:14px;width:715px;height:49px;background:var(--white);border-bottom:1px solid #e5e5e5}
.brand{position:absolute;left:103px;top:16px;display:flex;align-items:center;gap:5px;font-family:"Montserrat",sans-serif;font-weight:700;font-size:12px;color:var(--navy)}
.brand i{width:10px;height:10px;border-radius:50%;background:var(--blue)}
.nav{position:absolute;left:370px;top:19px;display:flex;gap:17px;font-size:7.3px;color:var(--ink)}
.nav .active{color:var(--navy)}
.nav-dot{position:absolute;left:587px;top:16px;width:18px;height:18px;border:1.5px solid var(--navy);border-radius:50%}

.hero{left:0;top:63px;width:715px;height:345px;background:linear-gradient(180deg,#7fb4dc 0%,#b9d6ea 45%,#7fae55 62%,#5f9a3a 100%)}
.hero-arrow{top:218px;width:22px;height:24px;background:rgba(20,30,45,.75);display:flex;align-items:center;justify-content:center}
.hero-title{left:95px;top:221px;font-family:"Montserrat",sans-serif;font-weight:700;font-size:18.5px;line-height:23px;color:var(--white)}
.hero-sub{left:96px;top:272px;font-family:"Montserrat",sans-serif;font-weight:500;font-size:10.5px;line-height:12px;color:var(--white)}
.btn{display:flex;align-items:center;justify-content:center;font-size:7px;color:var(--white);font-family:"Montserrat",sans-serif}
.btn-learn{left:96px;top:306px;width:77px;height:22px;background:var(--navy)}
.btn-demo{left:179px;top:306px;width:77px;height:22px;border:1.5px solid var(--white)}

.band{left:0;top:408px;width:715px;height:356px;background:var(--pale)}
.service{top:374px;width:129px;height:136px;clip-path:polygon(0 0,100% 14px,100% 100%,0 100%);color:var(--white);text-align:center}
.service.light{background:var(--blue)}
.service.dark{background:var(--navy)}
.service svg{margin-top:26px}
.service h3{font-family:"Montserrat",sans-serif;font-weight:500;font-size:8.5px;margin-top:10px;letter-spacing:.2px}
.service p{font-size:5.6px;line-height:10.5px;margin:6px 8px 0}
.plus{top:494px;width:34px;height:34px;border-radius:50%;display:flex;align-items:center;justify-content:center;color:var(--white);font-size:14px;font-weight:300}

.welcome{left:96px;top:538px;width:523px;height:208px;background:var(--white);box-shadow:0 2px 8px rgba(0,80,140,.08)}
.welcome h2{position:absolute;left:0;width:100%;top:24px;text-align:center;font-family:"Montserrat",sans-serif;font-weight:600;font-size:16px;color:var(--blue)}
.welcome h4{position:absolute;left:0;width:100%;top:47px;text-align:center;font-family:"Montserrat",sans-serif;font-weight:400;font-size:10px;color:var(--ink)}
.rule{position:absolute;height:2px;width:16px;background:var(--blue)}
.welcome-name{position:absolute;left:66px;top:104px;font-family:"Montserrat",sans-serif;font-weight:700;font-size:14px;color:var(--navy);display:flex;align-items:center;gap:6px;white-space:nowrap}
.welcome-name i{width:14px;height:14px;background:var(--blue);border-radius:50%}
.welcome p{position:absolute;left:203px;top:90px;width:255px;font-size:6px;line-height:10.8px;text-align:justify;color:var(--ink)}
.read{position:absolute;left:203px;top:136px;width:48px;height:15px;background:var(--blue);color:var(--white);font-size:6px;display:flex;align-items:center;justify-content:center;font-weight:600}
.dots{position:absolute;left:249px;top:178px;display:flex;gap:5px}
.dots i{width:4px;height:4px;border-radius:50%;background:var(--blue)}

.blog-title{left:0;width:715px;top:780px;text-align:center;font-family:"Montserrat",sans-serif;font-weight:400;font-size:10.5px;color:var(--ink)}
.post{top:815px;width:162px}
.post .media{width:162px;height:107px;border:2px solid #e6e6e6;position:relative}
.post .date{position:absolute;left:3px;top:3px;width:21px;height:28px;background:var(--navy);color:var(--white);text-align:center;font-family:"Montserrat",sans-serif}
.post .date b{display:block;font-size:11px;line-height:14px}
.post .date span{display:block;font-size:6px}
.post h5{font-family:"Montserrat",sans-serif;font-weight:500;font-size:9.8px;margin-top:10px}
.post p{font-size:5.4px;line-height:11.5px;margin-top:5px;color:var(--muted);font-weight:600}
.post hr{border:none;border-top:1px solid var(--line);margin-top:6px;width:157px}
.post .meta{font-size:5.6px;color:var(--muted);margin-top:7px;display:flex;gap:8px}
.post .meta span{display:flex;align-items:center;gap:3px}

.footer{left:0;top:1032px;width:715px;height:144px;background:linear-gradient(180deg,#eef8fd,#e1f2fb)}
.footer h6{position:absolute;top:27px;font-family:"Montserrat",sans-serif;font-weight:500;font-size:8.5px;color:var(--ink)}
.links{position:absolute;left:107px;top:46px;list-style:none;font-size:5.6px;font-weight:600}
.links li{height:16px;display:flex;align-items:center;gap:6px}
.email-field{position:absolute;left:213px;top:42px;width:100px;height:14px;background:var(--white);border:1px solid #ddd;font-size:5.5px;padding:3px 4px}
.subscribe{position:absolute;left:214px;top:59px;width:52px;height:14px;background:var(--blue);color:var(--white);font-size:5.8px;font-weight:600;display:flex;align-items:center;justify-content:center}
.social{position:absolute;top:85px;width:20px;height:20px;border:1px solid #d5dde3;background:var(--white)}
.social.main{background:var(--deep);border-color:var(--deep)}
.contact{position:absolute;left:362px;font-size:5.8px;color:var(--ink);display:flex;gap:7px;line-height:13px}
.map{position:absolute;left:482px;top:31px;width:124px;height:90px;border:2px solid #fff;background:linear-gradient(135deg,#e8e4dc,#d7e6cf)}
.copy{left:0;top:1176px;width:715px;height:24px;background:var(--white);text-align:center;font-size:5.6px;font-weight:600;line-height:24px}
</style>
</head>
<body>

<div class="abs topbar">
  <span style="left:103px"><svg width="5" height="6" viewBox="0 0 10 12"><path d="M5 0a4 4 0 0 0-4 4c0 3 4 8 4 8s4-5 4-8a4 4 0 0 0-4-4z" fill="#0a5ea8"/></svg>Level 2, 14 Dune Rd, east harbor KO 4410</span>
  <span style="left:445px"><svg width="7" height="5" viewBox="0 0 14 10"><rect x=".5" y=".5" width="13" height="9" fill="none" stroke="#0a5ea8"/><path d="M.5.5 7 6 13.5.5" fill="none" stroke="#0a5ea8"/></svg>mara@harborlink.tech</span>
  <span style="left:539px"><svg width="6" height="6" viewBox="0 0 12 12"><path d="M2 1l3 0 1 3-2 1c1 2 2 3 4 4l1-2 3 1v3c-6 0-10-4-10-10z" fill="#0a5ea8"/></svg>Call Us :&nbsp; 08 5550 1824</span>
</div>

<header class="abs header">
  <div class="brand"><i></i>Harbor Link</div>
  <nav class="nav"><span class="active">Home</span><span>About Us</span><span>Services</span><span>Blog</span><span>Contact Us</span></nav>
  <div class="nav-dot"></div>
</header>

<section class="abs hero" role="img" aria-label="Businessman working on a laptop seated on grass in front of a city skyline under a blue sky"></section>
<div class="abs hero-arrow" style="left:0"><svg width="6" height="8" viewBox="0 0 6 8"><path d="M5 0 1 4l4 4" fill="none" stroke="#fff" stroke-width="1.3"/></svg></div>
<div class="abs hero-arrow" style="left:693px"><svg width="6" height="8" viewBox="0 0 6 8"><path d="M1 0l4 4-4 4" fill="none" stroke="#fff" stroke-width="1.3"/></svg></div>
<h1 class="abs hero-title">Harbor Link is an Information<br>Communication Technology</h1>
<p class="abs hero-sub">This business that aims to help small to medium businesses<br>unlock the power and benefits of the cloud.</p>
<a class="abs btn btn-learn">LEARN MORE</a>
<a class="abs btn btn-demo">LIVE DEMO</a>

<div class="abs band"></div>

<article class="abs service light" style="left:96px">
  <svg width="22" height="18" viewBox="0 0 22 18"><path d="M6 12a4 4 0 0 1 0-8 6 6 0 0 1 11 2 3 3 0 0 1 0 6z" fill="none" stroke="#fff" stroke-width="1.3"/><path d="M11 12v3M7 16h8" stroke="#fff" stroke-width="1.3"/></svg>
  <h3>CLOUD TECH</h3>
  <p>Neque porro quisquam est qui dolorem ipsum quia dolor sit amet, consectetur, adipisci velit...</p>
</article>
<article class="abs service dark" style="left:228px">
  <svg width="22" height="18" viewBox="0 0 22 18"><path d="M6 1h7l4 4v12H6z" fill="none" stroke="#fff" stroke-width="1.3"/><path d="M9 8h5M9 11h5M9 14h5" stroke="#fff"/></svg>
  <h3>INFORMATION</h3>
  <p>Neque porro quisquam est qui dolorem ipsum quia dolor sit amet, consectetur, adipisci velit...</p>
</article>
<article class="abs service light" style="left:359px">
  <svg width="22" height="18" viewBox="0 0 22 18"><path d="M3 7l8-6 8 6v10H3z" fill="none" stroke="#fff" stroke-width="1.3"/><path d="M3 7l8 6 8-6" fill="none" stroke="#fff" stroke-width="1.3"/></svg>
  <h3>COMMUNICATION</h3>
  <p>Neque porro quisquam est qui dolorem ipsum quia dolor sit amet, consectetur, adipisci velit...</p>
</article>
<article class="abs service dark" style="left:490px">
  <svg width="22" height="18" viewBox="0 0 22 18"><circle cx="11" cy="9" r="7.5" fill="none" stroke="#fff" stroke-width="2.5"/><circle cx="11" cy="9" r="3" fill="none" stroke="#fff" stroke-width="1.3"/></svg>
  <h3>SUPPORT</h3>
  <p>Neque porro quisquam est qui dolorem ipsum quia dolor sit amet, consectetur, adipisci velit...</p>
</article>
<span class="abs plus" style="left:144px;background:var(--blue)">+</span>
<span class="abs plus" style="left:275px;background:var(--navy)">+</span>
<span class="abs plus" style="left:406px;background:var(--blue)">+</span>
<span class="abs plus" style="left:537px;background:var(--navy)">+</span>

<section class="abs welcome">
  <h2>WELCOME</h2>
  <h4>ABOUT HARBOR LINK</h4>
  <span class="rule" style="left:254px;top:64px"></span>
  <div class="welcome-name"><i></i>Harbor Link</div>
  <p>Lorem Ipsum comes from sections 1.10.32 and 1.10.33 of "de Finibus Bonorum et Malorum" (The Extremes of Good and Evil) by Cicero, written in 45 BC. This book is a treatise on the theory of ethics, very popular during the Renaissance. The first line of Lorem Ipsum, "Lorem ipsum dolor sit amet..</p>
  <a class="read">READ MORE</a>
  <div class="dots"><i></i><i></i><i></i></div>
</section>

<h2 class="abs blog-title">BLOG</h2>
<span class="abs rule" style="left:350px;top:797px"></span>

<article class="abs post" style="left:104px">
  <div class="media" role="img" aria-label="Illustration of a relaxed businessman lounging on a cloud" style="background:linear-gradient(160deg,#8ec3c5,#6fa9ac)"><div class="date"><b>01</b><span>NOV</span></div></div>
  <h5>Finibus Bonorum et Malorum</h5>
  <p>Nam libero tempore, cum soluta nobis est eligendi optio cumque nihil impedit quo minus id quod maxim.</p>
  <hr>
  <div class="meta"><span>&#9679; John Doe</span><span>&#9675; 3 Comments</span></div>
</article>
<article class="abs post" style="left:278px">
  <div class="media" role="img" aria-label="Photo of a young woman reading her phone outdoors" style="background:linear-gradient(160deg,#b06a3c,#6b4a36)"><div class="date"><b>01</b><span>NOV</span></div></div>
  <h5>Finibus Bonorum et Malorum</h5>
  <p>Nam libero tempore, cum soluta nobis est eligendi optio cumque nihil impedit quo minus id quod maxim.</p>
  <hr>
  <div class="meta"><span>&#9679; John Doe</span><span>&#9675; 3 Comments</span></div>
</article>
<article class="abs post" style="left:451px">
  <div class="media" role="img" aria-label="Photo of a smiling businesswoman with glasses and floating cloud icons" style="background:linear-gradient(160deg,#a9d3ea,#dfeef6)"><div class="date"><b>01</b><span>NOV</span></div></div>
  <h5>Finibus Bonorum et Malorum</h5>
  <p>Nam libero tempore, cum soluta nobis est eligendi optio cumque nihil impedit quo minus id quod maxim.</p>
  <hr>
  <div class="meta"><span>&#9679; John Doe</span><span>&#9675; 3 Comments</span></div>
</article>

<footer class="abs footer">
  <h6 style="left:104px">Quick Links</h6>
  <ul class="links">
    <li>&rsaquo;<span>Home</span></li><li>&rsaquo;<span>About Us</span></li><li>&rsaquo;<span>Services</span></li><li>&rsaquo;<span>Blog</span></li><li>&rsaquo;<span>Contact Us</span></li>
  </ul>
  <h6 style="left:212px">Newsletter</h6>
  <div class="email-field">Enter Email id</div>
  <a class="subscribe">Subscribe</a>
  <span class="social main" style="left:216px"></span>
  <span class="social" style="left:243px"></span>
  <span class="social" style="left:270px"></span>
  <span class="social" style="left:297px"></span>
  <h6 style="left:362px">Contact Us</h6>
  <div class="contact" style="top:44px"><span>&#9742;</span><span>Phone : 08 5550 1824</span></div>
  <div class="contact" style="top:60px"><span>&#9993;</span><span>Email : mara@harborlink.tech</span></div>
  <div class="contact" style="top:82px"><svg width="6" height="8" viewBox="0 0 10 12" style="margin-top:2px"><path d="M5 0a4 4 0 0 0-4 4c0 3 4 8 4 8s4-5 4-8a4 4 0 0 0-4-4z" fill="#222"/></svg><span>Address :<br>Level 2, 14 Dune Rd,<br>east harbor KO 4410</span></div>
  <div class="map" role="img" aria-label="Street map showing the office location"></div>
</footer>
<div class="abs copy">© 2016. www.harborlinkko.com</div>

</body>
</html>
```